sydney wedding photography business needs a business card design

we need a business card design for a sydney based wedding photography and videography business. our business name is :golden hour photography and video. our target clients are 24-35 yrs female. our style is candid, organic, natural, dynamic. we are a team of young photographers and videographers, and help brides to create memories that they will cherish for the rest of their lives. the logo will be provided. we want an elegant design that reflects our style, and also want to give a great impression to our clients that we are one of the best studios in sydney and our brand means quality and premium service.

Target Market(s)

bride to be, 24-35 years old, living in sydney and surrunding areas

Industry/Entity Type

Wedding Photography

Contact Information for Business Card

address: 57 marrow lane, bexton nsw 2041
mobile: 0431872056
phone: (02) 9361 2748
info@goldenhourstudio.net.au
www.goldenhourstudio.net.au
facebook:goldenhourbridals
instagram:goldenhourbridals

Font styles to use
Serif
Sans Serif

Requirements
Nice to have
• maybe add my slogan"memories beyond eternity" if the layout looks good
Should not have
• no black color, not good idea for wedding biz card

```html
<!DOCTYPE html>
<html lang="en">
<head>
<meta charset="utf-8">
<title>Golden Hour Photography and Video – Business Card</title>
<link rel="stylesheet" href="https://fonts.googleapis.com/css2?family=EB+Garamond:wght@400;600&family=Montserrat:wght@400&display=swap">
<style>
  :root {
    --backdrop: #4b3024;
    --card: #f6efe2;
    --card-edge: #e4d6bd;
    --gold: #b8861b;
    --gold-soft: #a27a2c;
    --ink: #6b5230;
  }
  * { margin: 0; padding: 0; box-sizing: border-box; }
  html, body { width: 1200px; height: 864px; overflow: hidden; }
  body {
    background: var(--backdrop);
    display: flex;
    align-items: center;
    justify-content: center;
    gap: 48px;
    font-family: "EB Garamond", Georgia, serif;
    color: var(--gold);
  }
  .card {
    width: 540px;
    height: 309px;
    background: var(--card);
    border: 1px solid var(--card-edge);
    border-radius: 3px;
    box-shadow: 0 18px 40px rgba(0,0,0,.35);
    position: relative;
  }
  .brand { text-align: center; }
  .brand-name {
    font-family: "EB Garamond", Georgia, serif;
    font-weight: 600;
    color: var(--gold);
    white-space: nowrap;
    display: flex;
    align-items: center;
    justify-content: center;
    gap: 10px;
    line-height: 1;
  }
  .brand-dot {
    width: 10px; height: 10px;
    border-radius: 50%;
    background: var(--gold);
  }
  .brand-tag {
    font-family: "Montserrat", Arial, sans-serif;
    color: var(--gold-soft);
    text-transform: uppercase;
    white-space: nowrap;
  }

  /* front */
  .card-front { display: flex; align-items: center; justify-content: center; }
  .card-front .brand-name { font-size: 48px; }
  .card-front .brand-tag { font-size: 14px; letter-spacing: .45em; margin-top: 12px; padding-left: .45em; }

  /* back */
  .card-back .brand {
    position: absolute;
    top: 26px; right: 32px;
  }
  .card-back .brand-name { font-size: 32px; }
  .card-back .brand-tag { font-size: 9.5px; letter-spacing: .4em; margin-top: 7px; padding-left: .4em; }
  .holder {
    position: absolute;
    top: 112px; left: 0; right: 0;
    text-align: center;
    font-size: 24px;
    color: var(--gold-soft);
    line-height: 1.2;
  }
  .contacts {
    position: absolute;
    left: 24px; right: 24px; bottom: 22px;
    display: grid;
    grid-template-columns: 0.8fr 1.25fr 1.25fr;
    column-gap: 10px;
    row-gap: 12px;
  }
  .contact { text-align: center; min-width: 0; }
  .contact-label {
    font-size: 10.5px;
    text-transform: uppercase;
    letter-spacing: .06em;
    color: var(--gold);
    margin-bottom: 2px;
  }
  .contact-value {
    font-size: 12.5px;
    color: var(--ink);
    white-space: nowrap;
    line-height: 1.25;
  }
</style>
</head>
<body>
  <section class="card card-front" aria-label="Card front">
    <div class="brand">
      <div class="brand-name"><span class="brand-dot"></span>Golden Hour</div>
      <div class="brand-tag">Photography and Video</div>
    </div>
  </section>

  <section class="card card-back" aria-label="Card back">
    <div class="brand">
      <div class="brand-name"><span class="brand-dot"></span>Golden Hour</div>
      <div class="brand-tag">Photography and Video</div>
    </div>
    <p class="holder">Liam Carter/Photography</p>
    <div class="contacts">
      <div class="contact">
        <div class="contact-label">Mobile</div>
        <div class="contact-value">0431 872 056</div>
      </div>
      <div class="contact">
        <div class="contact-label">E-mail</div>
        <div class="contact-value">info@goldenhourstudio.net.au</div>
      </div>
      <div class="contact">
        <div class="contact-label">Address</div>
        <div class="contact-value">57 Marrow Lane, Bexton NSW 2041</div>
      </div>
      <div class="contact">
        <div class="contact-label">Phone</div>
        <div class="contact-value">(02) 9361 2748</div>
      </div>
      <div class="contact">
        <div class="contact-label">Website</div>
        <div class="contact-value">www.goldenhourstudio.net.au</div>
      </div>
      <div class="contact">
        <div class="contact-label">Facebook / Instagram</div>
        <div class="contact-value">goldenhourbridals</div>
      </div>
    </div>
  </section>
</body>
</html>
```